" Leia o briefing antes de produzir, as informações contidas são FUNDAMENTAIS para o desenvolvimento das peças. - É uma creche que atua com bebês e crianças até 5 anos. "

```html
<!DOCTYPE html>
<html lang="pt-BR">
<head>
<meta charset="utf-8">
<title>Fachada – Berçário Infantil</title>
<link rel="stylesheet" href="https://fonts.googleapis.com/css2?family=Alfa+Slab+One&family=Oswald:wght@600&family=Nunito:wght@600;800&display=swap">
<style>
  :root{
    --white:#ffffff;
    --red:#e4262d;
    --navy:#1b3f8f;
    --sky-top:#3f7fd0;
    --sky-mid:#8fbcea;
    --sky-light:#d9ebfa;
    --wall:#dcedf8;
    --wall-light:#eef7fd;
    --green:#9ccb3b;
    --yellow:#f6ea1a;
    --ink:#2a2a2a;
    --orange:#f07d1d;
    --blue-text:#1c7fbf;
    --paving-dark:#7c8794;
    --paving-light:#bcc5cf;
  }
  *{margin:0;padding:0;box-sizing:border-box}
  html,body{width:1200px;height:1200px;overflow:hidden;background:var(--white)}
  .facade{position:relative;width:1200px;height:1200px;background:var(--white)}

  .sky{
    position:absolute;left:0;top:156px;width:1200px;height:240px;
    background:
      radial-gradient(ellipse 260px 150px at 660px 0px, rgba(255,255,255,.95), rgba(255,255,255,0) 70%),
      linear-gradient(180deg,var(--sky-top) 0%,var(--sky-mid) 55%,var(--sky-light) 100%);
  }
  .sign-title{
    position:absolute;left:44px;top:206px;
    font-family:"Alfa Slab One",serif;font-size:150px;line-height:1;
    color:var(--red);letter-spacing:4px;
    transform:scaleX(.72);transform-origin:left top;
    -webkit-text-stroke:4px var(--white);paint-order:stroke fill;
  }
  .brand{
    position:absolute;left:768px;top:163px;width:274px;height:274px;border-radius:50%;
    background:var(--navy);border:8px solid var(--white);
    display:flex;align-items:center;justify-content:center;
  }
  .brand-name{
    font-family:"Nunito",sans-serif;font-weight:800;font-size:40px;line-height:1.05;
    color:var(--white);text-align:center;
  }
  .stripe-thick{position:absolute;left:0;top:380px;width:1200px;height:18px;background:var(--red)}
  .stripe-thin{position:absolute;left:0;top:405px;width:1200px;height:5px;background:var(--red)}
  .service-band{position:absolute;left:0;top:410px;width:1200px;height:106px;background:var(--white)}
  .service-name{
    position:absolute;left:24px;top:418px;
    font-family:"Oswald",sans-serif;font-weight:600;font-size:60px;line-height:1.4;color:var(--ink);
  }
  .stripe-bottom{position:absolute;left:0;top:516px;width:1200px;height:10px;background:var(--red)}
  .wall{
    position:absolute;left:0;top:540px;width:1200px;height:362px;
    background:linear-gradient(135deg,var(--wall-light),var(--wall));
  }
  .door{position:absolute;background:var(--green);border:14px solid var(--yellow)}
  .door-garage{left:34px;top:630px;width:436px;height:290px}
  .door-entry{left:494px;top:590px;width:144px;height:330px}
  .slats{position:absolute;left:0;right:0;bottom:12px;height:110px;
    background:repeating-linear-gradient(180deg,transparent 0 18px,rgba(0,0,0,.18) 18px 21px)}
  .tagline{
    position:absolute;left:680px;top:618px;
    font-family:"Nunito",sans-serif;font-weight:600;font-size:56px;line-height:76px;color:var(--blue-text);
  }
  .tagline .lead{color:var(--orange)}
  .paving{
    position:absolute;left:0;top:900px;width:1200px;height:146px;
    background:linear-gradient(180deg,var(--paving-dark),var(--paving-light));
  }
</style>
</head>
<body>
<main class="facade">
  <div class="sky" role="img" aria-label="Céu azul com sol brilhando"></div>
  <h1 class="sign-title">INFANTIL</h1>
  <div class="brand"><span class="brand-name">RODA<br>MÁGICA</span></div>
  <div class="stripe-thick"></div>
  <div class="stripe-thin"></div>
  <div class="service-band"></div>
  <p class="service-name">BERCARIO</p>
  <div class="stripe-bottom"></div>
  <div class="wall" role="img" aria-label="Parede com padrão de losangos azul-claro"></div>
  <div class="door door-garage"></div>
  <div class="door door-entry"><div class="slats"></div></div>
  <p class="tagline"><span class="lead">‘Era uma vez...</span><br>o mundo mágico<br>da fantasia!’</p>
  <div class="paving" role="img" aria-label="Calçada de blocos intertravados cinza"></div>
</main>
</body>
</html>
```